Newsletter Banner Ad with a URL to our website offering

We need a banner ad for a newsletter that is published to members biweekly that simply articulates our value proposition and enables the reader to click on our logo to learn more and engage with us to schedule an Emergency Response Plan so they are ready for when a burst pipe happens on their property. They will have a plan after they engage with us.
We need quotes to build two options 1&2

```html
<!DOCTYPE html>
<html lang="en">
<head>
<meta charset="utf-8">
<title>Brentwood Restoration Group – Rapid Response Plan</title>
<link rel="stylesheet" href="https://fonts.googleapis.com/css2?family=Montserrat:wght@800;900&display=swap">
<style>
  :root {
    --navy: #1d2f6b;
    --red: #c8232f;
    --white: #ffffff;
    --photo-light: #c9c1b5;
    --photo-mid: #8f8171;
    --photo-dark: #4f443a;
  }
  * { margin: 0; padding: 0; box-sizing: border-box; }
  html, body { width: 1200px; height: 310px; overflow: hidden; background: var(--white); }
  .banner {
    position: relative;
    display: block;
    width: 1200px;
    height: 310px;
    overflow: hidden;
    font-family: "Montserrat", Arial, sans-serif;
    background: var(--white);
    text-decoration: none;
  }
  .hero-scene {
    position: absolute;
    left: 380px; top: 0;
    width: 820px; height: 310px;
    background:
      linear-gradient(180deg, rgba(0,0,0,0.05) 0%, rgba(0,0,0,0) 40%, rgba(40,30,20,0.35) 100%),
      linear-gradient(90deg, var(--photo-dark) 0%, var(--photo-light) 45%, var(--photo-mid) 75%, var(--photo-dark) 100%);
  }
  .shapes { position: absolute; inset: 0; }
  .brand {
    position: absolute;
    left: 45px; top: 42px;
    width: 280px;
    text-align: center;
    color: var(--navy);
    font-weight: 900;
  }
  .brand-mark {
    display: block;
    width: 110px; height: 110px;
    margin: 0 auto 36px;
    border-radius: 50%;
    background: var(--navy);
  }
  .brand-name { display: block; font-size: 42px; line-height: 1; letter-spacing: 1px; white-space: nowrap; }
  .brand-tagline { display: block; font-size: 19px; line-height: 1; margin-top: 12px; letter-spacing: 1.5px; white-space: nowrap; }
  .headline {
    position: absolute;
    left: 563px; top: 100px;
    color: var(--white);
    font-weight: 900;
    text-transform: uppercase;
    text-shadow: 0 2px 6px rgba(0,0,0,0.35);
  }
  .headline-line { display: block; white-space: nowrap; }
  .headline-line--first { font-size: 47px; line-height: 1.1; }
  .headline-line--second { font-size: 38px; line-height: 1.1; margin-left: 22px; margin-top: 8px; }
</style>
</head>
<body>
<a class="banner" href="#">
  <div class="hero-scene" role="img" aria-label="Photo of a flooded commercial hallway with standing water on the floor"></div>

  <svg class="shapes" width="1200" height="310" viewBox="0 0 1200 310" aria-hidden="true">
    <path d="M0 0 H430 C395 80 395 230 445 310 H0 Z" fill="var(--white)"/>
    <path d="M430 0 C395 80 395 230 445 310" fill="none" stroke="var(--red)" stroke-width="10"/>
    <path d="M330 0 Q420 55 490 40 T900 18 H1200 V0 Z" fill="var(--red)"/>
    <path d="M820 0 H1200 V42 Q1000 14 820 0 Z" fill="var(--navy)"/>
    <circle cx="465" cy="292" r="37" fill="none" stroke="var(--navy)" stroke-width="5"/>
    <circle cx="425" cy="312" r="31" fill="var(--navy)"/>
    <circle cx="505" cy="312" r="22" fill="none" stroke="var(--white)" stroke-width="4"/>
  </svg>

  <div class="brand">
    <span class="brand-mark"></span>
    <span class="brand-name">BRENTWOOD</span>
    <span class="brand-tagline">RESTORATION GROUP</span>
  </div>

  <h1 class="headline">
    <span class="headline-line headline-line--first">Do you have a rapid</span>
    <span class="headline-line headline-line--second">response plan for this?</span>
  </h1>
</a>
</body>
</html>
```